Mobile Charts

Context:
I have built a mobile app using flex that shows charts based on some selections. It has 2 screens (Attached), the slash screen and the graphs screen. I also attached the photoshop file for the splash screen. The company name is "Plorvex", the product name is "Amber Kite"

I need to take the design to the next level as far as professionalism. The look should match some top analytics companies products. It should exude precision and professionalism.

Most rework will be done with the splash screen (photo shop attached). The splash screen is a 840 by 690) png that contains the instruction text as well as the Product logo and company logo.

Specific deliverables in order (feel free to do only the top 3, bonus points for the others):
1. Product Icon for "Amber Kite". The current icon being used is just a place holder (on the splash screen). We need something simple that will work in both the splash screen and to launch the application.
It should be this image: http://www.grivolart.example/file/red-sphere.jpg
with a white "AK" inside of it.

2. Company Logo for Plorvex. The current font being used works ok, but maybe something with more flare. Whatever you come up with should be in the splash screen.

3. Better placement / font selection / font size for the instructions. Maybe a box around each instruction as well. Feel free to kill the carrots/arrows.

4. Font selection: Which font family/ size/ color would you recommend for each text outside of the splash screen.

5. Button shape/color changes: Whats a better look for the list buttons or back button. If you make a change here I need pngs for the up and selected state.

Target Market(s)

executives at companies that develop games or freemium apps

Industry/Entity Type

Shop

Font styles to use
Sans Serif

Colors
ec2027
ffffff

Requirements
Must have
• Must look clean / professional. Product logo, company logo, new splash page.
Nice to have
• font selections

```html
<!DOCTYPE html>
<html lang="en">
<head>
<meta charset="utf-8">
<title>Amber Kite by Plorvex</title>
<link href="https://fonts.googleapis.com/css2?family=Source+Sans+3:wght@300;400&display=swap" rel="stylesheet">
<style>
  :root {
    --page-bg: #f3f3f3;
    --window-bg: #f5f5f5;
    --top-bar: #231f20;
    --title-bar: #e6e7e8;
    --text-dark: #333333;
    --text-muted: #8a8a8a;
    --text-faint: #bbbbbb;
    --grid: #d9d9d9;
    --line: #d81b5a;
    --button-bg: #ffffff;
    --button-border: #dcdcdc;
    --button-soft: #eeddd6;
    --button-active: #f9bfaa;
  }
  html, body {
    margin: 0;
    width: 1200px;
    height: 1200px;
    overflow: hidden;
  }
  body {
    position: relative;
    background: radial-gradient(circle at 50% 45%, #ffffff 0%, var(--page-bg) 70%);
    font-family: "Source Sans 3", "Source Sans Pro", sans-serif;
    color: var(--text-dark);
  }
  .app-window {
    position: absolute;
    left: 27px;
    top: 80px;
    width: 1143px;
    height: 857px;
    background: radial-gradient(circle at 55% 40%, #ffffff 0%, var(--window-bg) 65%);
    box-shadow: 0 1px 4px rgba(0,0,0,0.35);
  }
  .top-bar {
    height: 17px;
    background: var(--top-bar);
  }
  .title-bar {
    height: 43px;
    background: var(--title-bar);
    display: flex;
    align-items: center;
    justify-content: center;
    font-size: 18px;
    font-weight: 400;
    color: #333;
  }
  .session-list {
    position: absolute;
    left: 13px;
    top: 121px;
    margin: 0;
    padding: 0;
    list-style: none;
  }
  .session-button {
    width: 213px;
    height: 42px;
    box-sizing: border-box;
    margin-bottom: 7.3px;
    border: 1px solid var(--button-border);
    border-radius: 8px;
    background: var(--button-bg);
    box-shadow: 0 1px 2px rgba(0,0,0,0.12);
    display: flex;
    align-items: center;
    justify-content: center;
    font-size: 19.5px;
    color: var(--text-dark);
  }
  .session-button.is-hover { background: var(--button-soft); }
  .session-button.is-selected { background: var(--button-active); }
  .chart {
    position: absolute;
    left: 0;
    top: 0;
  }
  .axis-label {
    font-size: 16px;
    fill: var(--text-muted);
    font-weight: 300;
  }
  .tip-primary { font-size: 19px; fill: var(--text-dark); }
  .tip-secondary { font-size: 19px; fill: var(--text-faint); }
</style>
</head>
<body>
  <div class="app-window">
    <div class="top-bar"></div>
    <header class="title-bar">Amber Kite by Plorvex</header>
    <ul class="session-list">
      <li class="session-button">16:32:04 - 2014/10/10</li>
      <li class="session-button">16:32:04 - 2014/10/10</li>
      <li class="session-button">16:32:04 - 2014/10/10</li>
      <li class="session-button is-hover">16:32:04 - 2014/10/10</li>
      <li class="session-button">16:32:04 - 2014/10/10</li>
      <li class="session-button">16:32:04 - 2014/10/10</li>
      <li class="session-button is-selected">16:32:04 - 2014/10/10</li>
      <li class="session-button">16:32:04 - 2014/10/10</li>
      <li class="session-button">16:32:04 - 2014/10/10</li>
      <li class="session-button">16:32:04 - 2014/10/10</li>
    </ul>
  </div>

  <svg class="chart" width="1200" height="1200" viewBox="0 0 1400 1400" aria-label="Growth line chart">
    <g class="grid" stroke="var(--grid)" stroke-width="1">
      <line x1="441" y1="236" x2="1292" y2="236"/>
      <line x1="441" y1="300" x2="1292" y2="300"/>
      <line x1="441" y1="363" x2="1292" y2="363"/>
      <line x1="441" y1="426" x2="1292" y2="426"/>
      <line x1="441" y1="489" x2="1292" y2="489"/>
      <line x1="441" y1="552" x2="1292" y2="552"/>
      <line x1="441" y1="615" x2="1292" y2="615"/>
      <line x1="441" y1="678" x2="1292" y2="678"/>
      <line x1="441" y1="741" x2="1292" y2="741"/>
      <line x1="441" y1="804" x2="1292" y2="804"/>
      <line x1="441" y1="867" x2="1292" y2="867"/>
      <line x1="441" y1="236" x2="441" y2="867"/>
      <line x1="950" y1="236" x2="950" y2="867"/>
    </g>
    <g class="axis-label" text-anchor="end">
      <text x="430" y="251">9000</text>
      <text x="430" y="313">8000</text>
      <text x="430" y="374">7000</text>
      <text x="430" y="436">6000</text>
      <text x="430" y="498">5000</text>
      <text x="430" y="559">4000</text>
      <text x="430" y="621">3000</text>
      <text x="430" y="683">2000</text>
      <text x="430" y="744">1000</text>
      <text x="430" y="806">0</text>
    </g>
    <g class="axis-label" text-anchor="middle">
      <text x="441" y="887">0</text><text x="477" y="887">2</text><text x="513" y="887">4</text>
      <text x="549" y="887">6</text><text x="585" y="887">8</text><text x="625" y="887">10</text>
      <text x="661" y="887">12</text><text x="697" y="887">14</text><text x="733" y="887">16</text>
      <text x="769" y="887">18</text><text x="805" y="887">20</text><text x="841" y="887">22</text>
      <text x="877" y="887">26</text><text x="913" y="887">28</text><text x="949" y="887">30</text>
      <text x="985" y="887">32</text><text x="1021" y="887">34</text><text x="1057" y="887">36</text>
      <text x="1093" y="887">38</text><text x="1129" y="887">40</text><text x="1165" y="887">42</text>
      <text x="1201" y="887">44</text><text x="1237" y="887">46</text>
    </g>
    <path d="M487 801 C 650 780, 860 730, 950 652 C 1040 580, 1110 450, 1184 287" fill="none" stroke="var(--line)" stroke-width="1.5"/>
    <circle cx="950" cy="652" r="8" fill="none" stroke="var(--line)" stroke-width="1.5"/>

    <g class="tooltip">
      <path d="M741 541 H961 Q973 541 973 553 V597 Q973 609 961 609 H927 V628 L900 609 H741 Q729 609 729 597 V553 Q729 541 741 541 Z" fill="#fff" stroke="#e2e2e2"/>
      <text class="tip-primary" x="748" y="568">16:32:04 - 2014/10/10</text>
      <text class="tip-secondary" x="748" y="592">16:32:04 - 2014/10/10</text>
    </g>
    <g class="tooltip">
      <path d="M938 692 H973 V674 L1000 692 H1158 Q1170 692 1170 704 V749 Q1170 761 1158 761 H938 Q926 761 926 749 V704 Q926 692 938 692 Z" fill="#fff" stroke="#e2e2e2"/>
      <text class="tip-primary" x="945" y="721">16:32:04 - 2014/10/10</text>
      <text class="tip-secondary" x="945" y="745">16:32:04 - 2014/10/10</text>
    </g>
  </svg>
</body>
</html>
```